use my brand and make an elegant business card  with it

Target Market(s)
male and female ' ages 25 to 45 age- who appreciate the highest quality goods, experiences, services, brands and relationships
Industry/Entity Type
Business
Requirements
Must have
- my logo integrated into the design-note the uploaded file
front: just logo and the phrase: Pure. Bold. Fine. Grace
back informations:
Mirela Dostan
Director
phone: +1 604 5290417
www.midostan.com
email: mireladostan@midostan.com
the pin of Facebook (F) and tweeter (T)
Nice to have
- contrast of the colors black gold and silver
Should not have
- cartoons or whimsical design

```html
<!DOCTYPE html>
<html lang="en">
<head>
<meta charset="utf-8">
<title>Mi Dostan — Business Card</title>
<link href="https://fonts.googleapis.com/css2?family=Cinzel:wght@400;600&family=Tinos&family=Lato:wght@700&display=swap" rel="stylesheet">
<style>
  :root {
    --bg: #e9e4dc;
    --card: #141414;
    --card-edge: #1f1f1f;
    --gold: #d9b81c;
    --silver: #b8b8b8;
    --grey: #8a8a8a;
    --shade: #3a3a3a;
  }
  * { margin: 0; padding: 0; box-sizing: border-box; }
  html, body { width: 1200px; height: 960px; overflow: hidden; }
  body {
    background: var(--bg);
    position: relative;
    font-family: "Tinos", serif;
  }
  .card {
    position: absolute;
    width: 560px;
    height: 320px;
    background: radial-gradient(circle at 40% 35%, var(--card-edge), var(--card) 75%);
    border-radius: 4px;
    box-shadow: 0 18px 40px rgba(0,0,0,.28);
    overflow: hidden;
  }
  /* Front */
  .card--front { left: 90px; top: 560px; }
  .front-pattern {
    position: absolute; inset: 0;
    background: repeating-linear-gradient(180deg, rgba(255,255,255,.035) 0 14px, rgba(255,255,255,0) 14px 28px);
  }
  .brand {
    position: absolute; left: 0; right: 0; top: 108px;
    text-align: center;
  }
  .brand-name {
    font-family: "Cinzel", serif;
    font-weight: 600;
    font-size: 54px;
    letter-spacing: 4px;
    color: var(--gold);
    line-height: 1;
  }
  .brand-tagline {
    margin-top: 14px;
    font-family: "Cinzel", serif;
    font-size: 17px;
    letter-spacing: 4px;
    color: var(--silver);
  }
  /* Back */
  .card--back { left: 550px; top: 90px; }
  .holder { position: absolute; left: 44px; top: 36px; }
  .holder-name {
    font-family: "Cinzel", serif;
    font-size: 26px;
    letter-spacing: 2px;
    color: var(--gold);
  }
  .holder-role {
    font-family: "Lato", sans-serif;
    font-weight: 700;
    font-size: 11px;
    letter-spacing: 1px;
    color: var(--grey);
    margin-top: 2px;
  }
  .contacts { position: absolute; left: 44px; top: 128px; list-style: none; }
  .contact {
    display: flex; align-items: center; gap: 12px;
    font-size: 19px; color: var(--silver);
    height: 28px;
  }
  .contact svg { width: 16px; height: 16px; flex: none; }
  .follow { display: flex; align-items: center; gap: 6px; }
  .social-pin { width: 14px; height: 14px; background: var(--gold); border-radius: 2px; }
  .crest {
    position: absolute; right: 0; top: 90px;
    width: 150px; height: 230px;
    background: radial-gradient(ellipse at 55% 45%, #4a4a4a, var(--shade) 60%, rgba(58,58,58,0) 80%);
  }
</style>
</head>
<body>
  <section class="card card--back">
    <div class="holder">
      <div class="holder-name">Mirela Dostan</div>
      <div class="holder-role">DIRECTOR</div>
    </div>
    <ul class="contacts">
      <li class="contact">
        <svg viewBox="0 0 16 16"><path d="M4 1.5l2.2 3-1.3 1.6c.8 1.9 2.2 3.3 4 4.1l1.6-1.3 3 2.2-1.2 2.6C6.6 13.4 2.6 9.4 1.4 3z" fill="var(--gold)"/></svg>
        +1 604 5290417
      </li>
      <li class="contact">
        <svg viewBox="0 0 16 16"><rect x="1" y="3" width="14" height="10" fill="none" stroke="var(--gold)" stroke-width="1.6"/><path d="M1 3l7 6 7-6" fill="none" stroke="var(--gold)" stroke-width="1.6"/></svg>
        mireladostan@midostan.com
      </li>
      <li class="contact">
        <svg viewBox="0 0 16 16"><circle cx="8" cy="8" r="6.8" fill="none" stroke="var(--gold)" stroke-width="1.6"/><ellipse cx="8" cy="8" rx="3" ry="6.8" fill="none" stroke="var(--gold)" stroke-width="1.2"/><path d="M1.5 8h13" stroke="var(--gold)" stroke-width="1.2"/></svg>
        www.midostan.com
      </li>
      <li class="contact follow">
        Follow me in :
        <span class="social-pin"></span>
        <span class="social-pin"></span>
      </li>
    </ul>
    <div class="crest" role="img" aria-label="Grey heraldic crest silhouette decoration"></div>
  </section>

  <section class="card card--front">
    <div class="front-pattern" role="img" aria-label="Faint repeated tagline text pattern in dark grey"></div>
    <div class="brand">
      <div class="brand-name">MI DOSTAN</div>
      <div class="brand-tagline">Pure. Bold. Fine. Grace</div>
    </div>
  </section>
</body>
</html>
```